New website for out outstanding veterinary training center

We already have a beautiful logo with nice colors and we are now looking for a breathtaking modern website to present our training center and future corses held there. A section to book open courses should also be available.

We are planing the realize the website with Wordpress.
The following pages should be available:
- Startpage / Overview
- Page to present the different rooms and seating option
- Page where the rooms can be booked
- Page where recommended accommodation are presented
- Page to present and book corses
- contact page
- Impressum

Target Market(s)

European Union

Industry/Entity Type

Education, Veterinary medicine

Number of Pages Required

5+ page

Font styles to use
Sans Serif

Colors
00AB8E
00BBA5
67D7C9
C6EFE9
E9F9F6

Requirements
Must have
• The website must be clear and easy to read. The colors form the logos should be used for the design.
Should not have
• To playful design. The page is not for a veterinary practice. we are a training center for veterinarians!

```html
<!DOCTYPE html>
<html lang="en">
<head>
<meta charset="utf-8">
<title>Veterra Academy – Veterinary Training Center</title>
<link rel="stylesheet" href="https://fonts.googleapis.com/css2?family=Lato:wght@400;700;900&display=swap">
<style>
:root{
  --teal:#158a80;
  --teal-dark:#0f6f67;
  --mint:#e9f9f6;
  --plum:#5b4b5d;
  --plum-dark:#4a3d4c;
  --ink:#1c1c1c;
  --text:#555;
  --muted:#888;
  --white:#fff;
}
*{box-sizing:border-box;margin:0;padding:0}
html,body{width:1200px;height:4484px;overflow:hidden}
body{font-family:'Lato',sans-serif;color:var(--ink);position:relative;background:var(--white)}
.abs{position:absolute}
.topbar{left:0;top:0;width:1200px;height:44px;background:var(--plum);color:#fff;font-size:15px;font-weight:700}
.topbar .welcome{left:111px;top:12px}
.topbar .lang{left:918px;top:0;width:170px;height:44px;background:#fff;color:#333;display:flex;align-items:center;justify-content:center;gap:10px;font-size:15px}
.lang .flag{width:22px;height:14px;background:linear-gradient(#c33 0 15%,#fff 15% 30%,#c33 30% 45%,#fff 45% 60%,#c33 60% 75%,#fff 75%);position:relative}
.lang .flag::before{content:"";position:absolute;left:0;top:0;width:10px;height:8px;background:#2b3f7a}
.header{left:0;top:44px;width:1200px;height:142px;background:#f4f4f4}
.corner-photo{top:44px;height:142px}
.brand{left:134px;top:52px;display:flex;flex-direction:column;align-items:center;gap:6px}
.brand .dot{width:74px;height:74px;border-radius:50%;background:var(--teal)}
.brand .name{font-size:22px;font-weight:700;color:var(--plum)}
.contact-line{top:104px;font-size:15px;color:#333;display:flex;align-items:center;gap:6px}
.nav{left:111px;top:174px;width:807px;height:52px;background:var(--plum-dark);clip-path:polygon(24px 0,100% 0,100% 100%,0 100%);display:flex;align-items:center;padding-left:34px;gap:0}
.nav a{color:#fff;text-decoration:none;font-size:15px;font-weight:700;padding:0 15px;height:52px;line-height:52px}
.nav a.active{background:var(--teal)}
.login{left:918px;top:174px;width:171px;height:52px;background:var(--teal);clip-path:polygon(0 0,100% 0,100% 100%,0 100%,0 0);color:#fff;font-weight:700;font-size:15px;display:flex;align-items:center;justify-content:center;gap:6px}
.login::after{content:"";position:absolute;right:0;top:0;width:30px;height:52px;background:#fff;clip-path:polygon(0 0,100% 100%,0 100%,0 0);opacity:0}
.hero{left:0;top:186px;width:1200px;height:793px;background:linear-gradient(100deg,#eef0ee 0%,#e4e6e2 40%,#cfd3cf 70%,#b8bfb7 100%)}
.hero h1{position:absolute;left:111px;top:285px;font-size:62px;font-weight:900;color:#111;letter-spacing:-1px}
.hero p{position:absolute;left:111px;top:366px;width:540px;font-size:15px;line-height:30px;color:#222}
.btn{display:inline-block;background:var(--teal);color:#fff;font-weight:700;font-size:16px;text-align:center}
.hero .btn{position:absolute;left:111px;top:446px;width:154px;height:52px;line-height:52px}
.arrow-btn{width:50px;height:50px;border:1.5px solid #444;display:flex;align-items:center;justify-content:center}
.sec-title{width:1200px;left:0;text-align:center;font-weight:900;font-size:40px;color:var(--ink)}
.rule{height:6px;width:84px;left:558px;background:var(--teal);border-radius:3px}
.intro{left:160px;top:1148px;width:880px;text-align:center;font-size:15px;line-height:31px;color:var(--text)}
.about-photo{left:111px;top:1237px;width:474px;height:397px;background:linear-gradient(135deg,#3f79b8 0%,#b7c9d9 45%,#e9d9bd 70%,#f1ece6 100%);box-shadow:0 4px 10px rgba(0,0,0,.2)}
.about-copy{left:617px;top:1274px;width:480px}
.about-copy h3{font-size:21px;font-weight:400;color:#333;margin-bottom:24px}
.about-copy p{font-size:13px;line-height:28px;color:var(--muted);margin-bottom:16px}
.about-copy li{list-style:none;font-size:14px;color:var(--muted);line-height:30px;display:flex;align-items:center;gap:6px}
.courses{left:0;top:1721px;width:1200px;height:697px;background:linear-gradient(160deg,#6a5b62 0%,#5a4c55 50%,#504551 100%)}
.courses .sec-title{color:#fff;top:96px}
.card{top:183px;width:317px;height:427px;background:#fff;border-radius:3px;padding:5px}
.card .pic{height:190px;background:linear-gradient(135deg,#f0f0ee,#d6dad8 60%,#aeb5b5)}
.card h4{font-size:15px;font-weight:700;color:#333;line-height:23px;margin:24px 9px 8px}
.card p{font-size:12.5px;line-height:24px;color:var(--muted);margin:0 9px 14px}
.card .btn{margin-left:9px;width:128px;height:44px;line-height:44px;font-size:15px}
.why{left:0;top:2418px;width:1200px;height:444px;background:linear-gradient(180deg,#168d82,#14827a 60%,#24706c)}
.why .sec-title{color:#fff;font-size:38px;top:98px}
.feature{top:192px;width:200px;text-align:center}
.feature .circle{width:114px;height:114px;border-radius:50%;background:#fff;margin:0 auto 16px;display:flex;align-items:center;justify-content:center}
.feature span{color:#fff;font-size:20px;font-weight:700}
.testi{top:3049px;width:319px;height:357px;background:var(--mint);padding:72px 42px 0}
.testi .quote{position:absolute;left:0;top:8px;font-size:54px;font-weight:900;color:#333;font-family:Georgia,serif}
.testi p{font-size:14.5px;line-height:24px;color:#444}
.testi .who{position:absolute;left:42px;bottom:30px;display:flex;align-items:center;gap:12px;font-size:12px;color:#444;line-height:16px}
.avatar{width:42px;height:42px;border-radius:50%;background:linear-gradient(#8b8f9a,#c8cbd1)}
.slider-arrow{top:3210px}
.field{background:#fff;border:1px solid #ccc;border-radius:4px;font-size:12px;color:#888;padding:0 12px;display:flex;align-items:center}
.contact-photo{left:638px;top:3629px;width:562px;height:496px;background:linear-gradient(150deg,#f2efe9 0%,#d9dfe6 40%,#3d6f97 70%,#a78b66 100%)}
.footer{left:0;top:4125px;width:1200px;height:359px;background:var(--plum);color:#fff}
.footer h5{font-size:15px;font-weight:700;margin-bottom:16px}
.footer li{list-style:none;font-size:13px;line-height:32px}
.footer .copy{position:absolute;left:0;width:1200px;top:325px;text-align:center;font-size:13px}
.footer hr{position:absolute;left:111px;top:300px;width:978px;border:0;border-top:1px solid rgba(255,255,255,.5)}
</style>
</head>
<body>

<div class="abs topbar">
  <div class="abs welcome">WELCOME TO VETERRA ACADEMY</div>
  <div class="abs lang"><span class="flag"></span>English</div>
</div>

<div class="abs header"></div>
<div class="abs corner-photo" role="img" aria-label="Cat photo" style="left:0;width:62px;background:linear-gradient(#eee,#b9ab9a)"></div>
<div class="abs corner-photo" role="img" aria-label="Dog photo" style="left:1114px;width:86px;background:linear-gradient(#f4f4f4,#c7884a)"></div>
<div class="abs brand"><span class="dot"></span><span class="name">Veterra Academy</span></div>
<div class="abs contact-line" style="left:605px">
  <svg width="10" height="14" viewBox="0 0 10 14"><path d="M5 0a5 5 0 0 0-5 5c0 4 5 9 5 9s5-5 5-9a5 5 0 0 0-5-5zm0 7a2 2 0 1 1 0-4 2 2 0 0 1 0 4z" fill="#158a80"/></svg>
  123, Lorem ipsum dolor sit amet, consectetur</div>
<div class="abs contact-line" style="left:968px">
  <svg width="13" height="13" viewBox="0 0 24 24"><path d="M6.6 10.8a15 15 0 0 0 6.6 6.6l2.2-2.2c.3-.3.7-.4 1-.2 1.1.4 2.3.6 3.6.6.6 0 1 .4 1 1V20c0 .6-.4 1-1 1A17 17 0 0 1 3 4c0-.6.4-1 1-1h3.5c.6 0 1 .4 1 1 0 1.3.2 2.5.6 3.6.1.3 0 .7-.2 1z" fill="#158a80"/></svg>
  123-456-7890</div>

<div class="abs hero" role="img" aria-label="Veterinarian working at a laptop beside a dog skeleton model">
  <h1>VETERRA</h1>
  <p>Sed ut perspiciatis unde omnis iste natus error sit accusantium doloremque laudantium, totam rem aperiam, eaque ipsa quae ab illo</p>
  <span class="btn">GET STARTED</span>
  <div class="abs arrow-btn" style="left:22px;top:373px"><svg width="26" height="18" viewBox="0 0 26 18"><path d="M9 1L1 9l8 8M1 9h24" stroke="#333" stroke-width="1.6" fill="none"/></svg></div>
  <div class="abs arrow-btn" style="left:1125px;top:373px"><svg width="26" height="18" viewBox="0 0 26 18"><path d="M17 1l8 8-8 8M25 9H1" stroke="#333" stroke-width="1.6" fill="none"/></svg></div>
</div>

<nav class="abs nav">
  <a class="active">HOME</a><a>WHO WE ARE</a><a>OUR COURSES</a><a>GET IN TOUCH</a><a>CONTACT</a>
</nav>
<div class="abs login">
  <svg width="14" height="14" viewBox="0 0 16 16"><circle cx="8" cy="8" r="7.5" fill="#fff"/><circle cx="8" cy="6" r="2.6" fill="#158a80"/><path d="M3.5 13a5 5 0 0 1 9 0" fill="#158a80"/></svg>LOG IN</div>

<h2 class="abs sec-title" style="top:1060px">WHO WE ARE</h2>
<div class="abs rule" style="top:1124px"></div>
<p class="abs intro">Lorem ipsum dolor sit amet, consectetur adipiscing elit, sed do eiusmod tempor incididunt ut labore et dolore magna aliqua. Ut enim ad minim veniam, quis nostrud exercitation ullamco laboris nisi ut aliquip ex ea commodo consequat.</p>
<div class="abs about-photo" role="img" aria-label="Puppy and kitten on an examination table with a vet behind"></div>
<div class="abs about-copy">
  <h3>Lorem ipsum dolor sit amet, consectetur</h3>
  <p>Sed ut perspiciatis unde omnis iste natus error sit voluptatem accusantium doloremque laudantium, totam rem aperiam, eaque ipsa quae ab illo inventore veritatis et quasi architecto beatae vitae dicta sunt explicabo.</p>
  <p>Sed ut perspiciatis unde omnis iste natus error sit voluptatem accusantium doloremque laudantium, totam rem aperiam,</p>
  <ul>
    <li><svg width="14" height="14" viewBox="0 0 14 14"><circle cx="7" cy="7" r="7" fill="#158a80"/><path d="M3.5 7l2.5 2.5 4.5-5" stroke="#fff" stroke-width="1.8" fill="none"/></svg>Lorem ipsum dolor sit amet, consectetur adipiscing</li>
    <li><svg width="14" height="14" viewBox="0 0 14 14"><circle cx="7" cy="7" r="7" fill="#158a80"/><path d="M3.5 7l2.5 2.5 4.5-5" stroke="#fff" stroke-width="1.8" fill="none"/></svg>Lorem ipsum dolor sit amet, consectetur adipiscing</li>
    <li><svg width="14" height="14" viewBox="0 0 14 14"><circle cx="7" cy="7" r="7" fill="#158a80"/><path d="M3.5 7l2.5 2.5 4.5-5" stroke="#fff" stroke-width="1.8" fill="none"/></svg>Lorem ipsum dolor sit amet, consectetur adipiscing</li>
  </ul>
</div>

<section class="abs courses" role="img" aria-label="Muted background photo of a dog">
  <h2 class="abs sec-title">OUR COURSES</h2>
  <div class="abs rule" style="top:134px"></div>
  <div class="abs card" style="left:113px">
    <div class="pic" role="img" aria-label="Veterinarian teaching in a clinic"></div>
    <h4>Lorem ipsum dolor sit amet, consectetur sit amet, consectetur</h4>
    <p>Lorem ipsum dolor sit amet, adipiscing elit, sed do eiusmod tempor incididunt ut labore et dolore magna aliqua.</p>
    <span class="btn">BUY NOW</span>
  </div>
  <div class="abs card" style="left:443px">
    <div class="pic" role="img" aria-label="Veterinarian examining a dog skeleton model"></div>
    <h4>Lorem ipsum dolor sit amet, consectetur sit amet, consectetur</h4>
    <p>Lorem ipsum dolor sit amet, adipiscing elit, sed do eiusmod tempor incididunt ut labore et dolore magna aliqua.</p>
    <span class="btn">BUY NOW</span>
  </div>
  <div class="abs card" style="left:772px">
    <div class="pic" role="img" aria-label="Veterinarian consulting with a dog owner"></div>
    <h4>Lorem ipsum dolor sit amet, consectetur sit amet, consectetur</h4>
    <p>Lorem ipsum dolor sit amet, adipiscing elit, sed do eiusmod tempor incididunt ut labore et dolore magna aliqua.</p>
    <span class="btn">BUY NOW</span>
  </div>
</section>

<section class="abs why" role="img" aria-label="Teal-tinted photo of a dog and cat under a blanket">
  <h2 class="abs sec-title">Why Choose Us</h2>
  <div class="abs feature" style="left:133px"><div class="circle"><svg width="56" height="52" viewBox="0 0 56 52"><g fill="#158a80"><ellipse cx="12" cy="20" rx="6" ry="8"/><ellipse cx="22" cy="8" rx="6" ry="8"/><ellipse cx="34" cy="8" rx="6" ry="8"/><ellipse cx="44" cy="20" rx="6" ry="8"/><path d="M28 24c-10 0-18 14-14 22 3 5 10 2 14 2s11 3 14-2c4-8-4-22-14-22z"/></g><path d="M28 31v11M22.5 36.5h11" stroke="#fff" stroke-width="3"/></svg></div><span>Lorem ipsum</span></div>
  <div class="abs feature" style="left:377px"><div class="circle"><svg width="50" height="50" viewBox="0 0 50 50" fill="none" stroke="#158a80" stroke-width="3"><rect x="8" y="16" width="34" height="30"/><rect x="14" y="4" width="22" height="12"/><path d="M25 6v8M21 10h8"/><rect x="30" y="32" width="8" height="14"/><circle cx="18" cy="31" r="3"/></svg></div><span>Lorem ipsum</span></div>
  <div class="abs feature" style="left:623px"><div class="circle"><svg width="50" height="50" viewBox="0 0 50 50" fill="none" stroke="#158a80" stroke-width="3"><path d="M10 6v12a8 8 0 0 0 16 0V6M18 26v8a10 10 0 0 0 20 0v-4"/><circle cx="38" cy="26" r="4"/></svg></div><span>Lorem ipsum</span></div>
  <div class="abs feature" style="left:867px"><div class="circle"><svg width="44" height="54" viewBox="0 0 44 54" fill="none" stroke="#158a80" stroke-width="3"><rect x="8" y="12" width="28" height="38" rx="3"/><rect x="14" y="4" width="16" height="8"/><path d="M14 22h16M14 28h16"/><circle cx="22" cy="41" r="4" fill="#158a80"/></svg></div><span>Lorem ipsum</span></div>
</section>

<h2 class="abs sec-title" style="top:2936px">Testimonials</h2>
<div class="abs" style="left:608px;top:3000px;width:66px;height:2px;background:#333"></div>
<svg class="abs slider-arrow" style="left:70px" width="14" height="24" viewBox="0 0 14 24"><path d="M12 2L2 12l10 10" stroke="#158a80" stroke-width="2" fill="none"/></svg>
<svg class="abs slider-arrow" style="left:1185px" width="14" height="24" viewBox="0 0 14 24"><path d="M2 2l10 10L2 22" stroke="#158a80" stroke-width="2" fill="none"/></svg>

<div class="abs testi" style="left:141px"><span class="quote">“</span>
  <p>But I must explain to you how all this mistaken idea of denou ncing pleasure and praising pain was born and I will give you a complete account of the sys tem, and expound the actual teachings of the great explorer of the truth.</p>
  <div class="who"><span class="avatar" role="img" aria-label="Portrait of Richard"></span><span>RICHARD<br>England</span></div></div>
<div class="abs testi" style="left:488px"><span class="quote">“</span>
  <p>But I must explain to you how all this mistaken idea of denou ncing pleasure and praising pain was born and I will give you a complete account of the sys tem, and expound the actual teachings of the great explorer of the truth.</p>
  <div class="who"><span class="avatar" role="img" aria-label="Portrait of Richard"></span><span>RICHARD<br>England</span></div></div>
<div class="abs testi" style="left:834px"><span class="quote">“</span>
  <p>But I must explain to you how all this mistaken idea of denou ncing pleasure and praising pain was born and I will give you a complete account of the system, and expound the actual teachings of the great explorer of the truth,</p>
  <div class="who"><span class="avatar" role="img" aria-label="Portrait of Richard"></span><span>RICHARD<br>England</span></div></div>

<h2 class="abs sec-title" style="top:3497px">GET IN TOUCH</h2>
<div class="abs rule" style="top:3561px"></div>
<div class="abs field" style="left:111px;top:3680px;width:232px;height:54px">First Name</div>
<div class="abs field" style="left:359px;top:3680px;width:232px;height:54px">Last Name</div>
<div class="abs field" style="left:111px;top:3748px;width:232px;height:54px">Email Address</div>
<div class="abs field" style="left:359px;top:3748px;width:232px;height:54px">Phone Number</div>
<div class="abs field" style="left:111px;top:3815px;width:480px;height:54px">Subject</div>
<div class="abs field" style="left:111px;top:3883px;width:480px;height:124px;align-items:flex-start;padding-top:18px">Message</div>
<div class="abs btn" style="left:111px;top:4022px;width:480px;height:54px;line-height:54px;border-radius:4px;font-size:18px">SUBMIT</div>
<div class="abs contact-photo" role="img" aria-label="Smiling veterinarian holding a pug in a clinic"></div>

<footer class="abs footer">
  <div class="abs" style="left:111px;top:52px;width:300px">
    <h5 style="font-size:22px">ABOUT</h5>
    <p style="font-size:13px;line-height:25px">Sed ut perspiciatis unde omnis iste natus error sit voluptatem accusantium doloremque laudantium, totam rem aperiam,</p>
  </div>
  <div class="abs" style="left:531px;top:50px"><h5>QUICK LINKS</h5>
    <ul><li>Home</li><li>Who we are</li><li>Our Courses</li><li>Get in touch</li><li>Contact</li></ul></div>
  <div class="abs" style="left:710px;top:50px"><h5>CONTACT</h5>
    <ul><li>123, Lorem ipsum dolor sit amet,</li><li>consectetur adipiscing</li><li>123-456-7890</li><li>info@veterra-academy.eu</li></ul></div>
  <div class="abs" style="left:1003px;top:50px"><h5>HELP US</h5>
    <ul><li>Privacy Policy</li><li>FAQ</li><li>Information</li></ul></div>
  <hr>
  <div class="copy">© 2021 All Rights Reserved</div>
</footer>

</body>
</html>
```